Container Web Design Project

I need the front page of my website to have a new, fresh look.
Our company is a highly specialized marketplace for shipping containers (yes, the 20' and 40' kind). Basically, think of Lokko for shipping containers.
I have all of the links/content that I need plugged into a wireframe (attached), and the core color (blue #0073a2) of our existing site should stay the same as we've got stationary, business cards, marketing materials...
If you have any questions please ask.

```html
<!DOCTYPE html>
<html lang="en">
<head>
<meta charset="utf-8">
<title>CrateHarbor.com – Shipping Container Marketplace</title>
<link rel="stylesheet" href="https://fonts.googleapis.com/css2?family=Roboto+Condensed:wght@400;700&family=Open+Sans:wght@400;600;700&family=Arimo:wght@400;700&display=swap">
<style>
:root{
  --brand:#0073a2;
  --brand-dark:#005d86;
  --brand-deep:#0a6390;
  --nav-top:#4fb0db;
  --nav-bottom:#2b94c6;
  --ink:#1c1c1c;
  --link:#1a7fb5;
  --panel:#f2f2f2;
  --panel-edge:#d6d6d6;
  --black:#0d0d0d;
  --white:#ffffff;
}
*{box-sizing:border-box;margin:0;padding:0}
html,body{width:932px;height:1200px;overflow:hidden}
body{background:var(--brand);font-family:"Open Sans",sans-serif;color:var(--ink);position:relative}
.abs{position:absolute}

/* header */
.site-header{left:108px;top:0;width:716px;height:57px;background:var(--white)}
.brand-name{left:10px;top:8px;font-family:"Roboto Condensed",sans-serif;font-weight:700;font-size:30px;color:var(--brand)}
.utility-links{right:10px;top:9px;font-size:9.5px;color:#222}
.utility-links span{margin:0 4px;color:#777}
.phone{right:8px;top:30px;font-family:"Arimo",sans-serif;font-weight:700;font-size:19px;color:var(--brand)}
.main-nav{left:108px;top:57px;width:716px;height:41px;background:linear-gradient(var(--nav-top),var(--nav-bottom));display:flex;box-shadow:0 2px 3px rgba(0,0,0,.3);overflow:hidden}
.main-nav a{flex:1 1 auto;font-family:"Roboto Condensed",sans-serif;font-size:11px;color:var(--white);text-decoration:none;display:flex;align-items:center;justify-content:center;padding:0 6px;border-right:1px solid rgba(255,255,255,.3);white-space:nowrap}
.main-nav a:last-child{border:none}

/* search */
.search-field{left:127px;top:117px;width:387px;height:27px;background:var(--black);border-radius:3px;color:#999;font-size:11px;padding:7px 10px}
.search-field svg{position:absolute;right:8px;top:5px}
.select{top:117px;height:27px;background:#f4f4f4;border-radius:2px;font-size:10px;color:#555;padding:7px 8px;white-space:nowrap}
.select .arrow{position:absolute;right:0;top:0;width:24px;height:27px;background:var(--black);display:flex;align-items:center;justify-content:center}
.search-btn{left:715px;top:117px;width:78px;height:27px;background:linear-gradient(#fff,#dcdcdc);border-radius:2px;font-family:"Arimo",sans-serif;font-weight:700;font-size:13px;color:var(--brand);text-align:center;line-height:27px}

/* sidebar */
.side-menu{left:108px;top:162px;width:182px}
.side-menu a{display:block;height:27px;margin-bottom:1.7px;background:linear-gradient(#f4f4f4,#d8d8d8);font-family:"Roboto Condensed",sans-serif;font-size:12px;color:#333;padding:6px 7px;text-decoration:none;white-space:nowrap}
.side-menu a.current{background:var(--white)}
.newsletter{left:108px;top:399px;width:182px;height:84px;background:linear-gradient(#f2f2f2,#d9d9d9)}
.newsletter h3{font-family:"Roboto Condensed",sans-serif;font-weight:400;font-size:13.5px;color:var(--brand-dark);margin:10px 0 0 7px}
.newsletter .field{position:absolute;left:8px;top:33px;width:167px;height:19px;background:#222;border-radius:3px}
.newsletter .submit{position:absolute;left:52px;top:57px;width:75px;height:20px;background:var(--brand);border-radius:3px;color:#fff;font-family:"Arimo",sans-serif;font-weight:700;font-size:13px;text-align:center;line-height:20px}
.promo{left:108px;top:494px;width:182px;height:75px;background:linear-gradient(#f6efdd,#c9b48d)}
.promo h4{font-family:"Roboto Condensed",sans-serif;font-size:19px;color:#222;margin:5px 0 0 9px;line-height:1}
.promo p{font-family:"Roboto Condensed",sans-serif;font-size:12.5px;color:#222;margin-left:9px}
.promo .more{position:absolute;left:10px;top:50px;background:#fff;color:var(--brand);font-size:9.5px;font-weight:700;padding:2px 7px;border-radius:2px}
.promo .tool-box{position:absolute;right:12px;top:42px;width:50px;height:28px;background:#c8302b}
.seller{left:108px;width:182px;height:74px;background:radial-gradient(#fff 30%,#cfcfcf);text-align:center;font-family:"Roboto Condensed",sans-serif;color:var(--brand-dark);padding-top:20px;line-height:1}
.seller b{font-size:19px;display:block}
.seller span{font-size:12.5px;font-weight:700}

/* content */
.map{left:297px;top:162px;width:527px;height:241px;background:linear-gradient(135deg,#ece6d6,#dfe8d2 60%,#c9dbe9)}
.product{top:411px;width:101px}
.product .thumb{height:91px;background:#fff;border-radius:2px;display:flex;align-items:center;justify-content:center}
.product .thumb div{width:64px;height:52px;border-radius:2px}
.product p{font-family:"Arimo",sans-serif;font-size:9.5px;color:#fff;line-height:11.5px}
.product p b{display:block;margin-top:5px}
.product p span{color:#111}

.listings{left:297px;top:578px;width:527px;height:400px;border-collapse:collapse;background:var(--panel);table-layout:fixed}
.listings th{height:33px;background:linear-gradient(#3b3b3b,#111);color:var(--link);font-family:"Arimo",sans-serif;font-weight:400;font-size:14px;text-align:left;padding-left:10px;border-right:1px solid #444}
.listings td{vertical-align:top;border-right:1px solid var(--panel-edge);border-top:1px solid var(--panel-edge);padding:15px 8px 0 10px;font-size:8.6px;line-height:11.5px;color:#222}
.listings td b{color:var(--link);font-weight:600}
.listings td.price{font-size:11px}
.listings .pic{display:block;width:78px;height:62px;border:2px solid #fff;box-shadow:0 0 2px #999;margin-top:-3px}

/* footer */
.legal{left:108px;top:994px;width:716px;height:65px;background:var(--brand-deep);color:#e8f2f8;font-size:10.5px;text-align:center;padding-top:14px;line-height:11.7px}
.footer-links{top:1080px;font-size:10.5px;color:#fff;line-height:18.7px}
.footer-brand{left:641px;top:1083px;width:183px;height:43px;border:2px solid #fff;border-radius:3px;font-family:"Roboto Condensed",sans-serif;font-weight:700;font-size:22px;color:#fff;text-align:center;line-height:39px}
.bottom-bar{left:108px;top:1162px;width:716px;height:38px;background:var(--black);color:#fff;font-size:10px;text-align:center;line-height:38px}
</style>
</head>
<body>

<header class="site-header abs">
  <div class="brand-name abs">CrateHarbor.com</div>
  <div class="utility-links abs">Create and Account<span>|</span>Login<span>|</span>About CrateHarbor.com<span>|</span>Contact Us</div>
  <div class="phone abs">(555) 014-2760</div>
</header>
<nav class="main-nav abs">
  <a>20' SHIPPING CONTAINERS</a><a>40' SHIPPING CONTAINERS</a><a>40' HIGH CUBE CONTAINERS</a><a>OPEN TOP CONTAINERS</a><a>HOW TO BUY A SHIPPING CONTAINER</a>
</nav>

<div class="search-field abs">City, State or Country
  <svg width="17" height="17" viewBox="0 0 17 17"><circle cx="7" cy="7" r="5.5" fill="none" stroke="#888" stroke-width="2"/><line x1="11" y1="11" x2="16" y2="16" stroke="#888" stroke-width="2.5"/></svg>
</div>
<div class="select abs" style="left:525px;width:110px">Container Type<span class="arrow"><svg width="12" height="8"><path d="M1 1l5 5 5-5" fill="none" stroke="#fff" stroke-width="2.5"/></svg></span></div>
<div class="select abs" style="left:641px;width:68px">Units<span class="arrow"><svg width="12" height="8"><path d="M1 1l5 5 5-5" fill="none" stroke="#fff" stroke-width="2.5"/></svg></span></div>
<div class="search-btn abs">Search</div>

<aside>
  <nav class="side-menu abs">
    <a>How to Buy Shipping Containers</a>
    <a class="current">New Listings</a>
    <a>News and Articles</a>
    <a>About CrateHarbor.com</a>
    <a>Container Weights and Dimensions</a>
    <a>CrateHarbor.com FAQs</a>
    <a>Shipping Container Terms</a>
    <a>How to Sell Your Containers</a>
  </nav>
  <div class="newsletter abs"><h3>Subscribe to Our Newsletter</h3><div class="field"></div><div class="submit">Submit</div></div>
  <div class="promo abs"><h4>Phasellus ut</h4><p>libero ut nulla</p><span class="more">Read More</span><div class="tool-box" role="img" aria-label="Red toolbox photo"></div></div>
  <div class="seller abs" style="top:577px"><b>Featured Seller</b><span>logo will come here</span></div>
  <div class="seller abs" style="top:662px"><b>Featured Seller</b><span>logo will come here</span></div>
  <div class="seller abs" style="top:747px"><b>Featured Seller</b><span>logo will come here</span></div>
</aside>

<main>
  <div class="map abs" role="img" aria-label="Street map of listing locations in central London"></div>

  <div class="product abs" style="left:297px"><div class="thumb"><div role="img" aria-label="Cardboard boxes photo" style="background:#c9965c"></div></div><p><b>Nam quis ligula</b><span>Container Type<br>Location:<br>Price: $00.00</span></p></div>
  <div class="product abs" style="left:404px"><div class="thumb"><div role="img" aria-label="Stacked boxes photo" style="background:#b98a5a"></div></div><p><b>Nam quis ligula</b><span>Container Type<br>Location:<br>Price: $00.00</span></p></div>
  <div class="product abs" style="left:511px"><div class="thumb"><div role="img" aria-label="Green shipping container photo" style="background:#5fbf3f"></div></div><p><b>Nam quis ligula</b><span>Container Type<br>Location:<br>Price: $00.00</span></p></div>
  <div class="product abs" style="left:617px"><div class="thumb"><div role="img" aria-label="White tissue box photo" style="background:#e6e6e6"></div></div><p><b>Nam quis ligula</b><span>Container Type<br>Location:<br>Price: $00.00</span></p></div>
  <div class="product abs" style="left:724px"><div class="thumb"><div role="img" aria-label="Red shipping container photo" style="background:#d3322a"></div></div><p><b>Nam quis ligula</b><span>Container Type<br>Location:<br>Price: $00.00</span></p></div>

  <table class="listings abs">
    <colgroup><col style="width:101px"><col style="width:143px"><col style="width:98px"><col style="width:88px"><col style="width:97px"></colgroup>
    <thead><tr><th></th><th>Listing Name</th><th>Container</th><th>Type</th><th>Price</th></tr></thead>
    <tbody>
      <tr><td><span class="pic" role="img" aria-label="Warehouse forklift photo" style="background:linear-gradient(#c98a3a,#6a5a3a)"></span></td><td><b>Nam quis ligula a nibh fermentum venenatis vitae</b> nec neque. Etiam non felis mi. Quisque feugiat, lectus non feugiat consectetur,</td><td><b>Nam quis ligula a</b> nec neque. Etiam non felis mi.</td><td><b>Nam quis ligula</b> nec neque. Etiam non felis mi.</td><td class="price">$ 00.00</td></tr>
      <tr><td><span class="pic" role="img" aria-label="Cardboard boxes photo" style="background:linear-gradient(#f0e4d4,#d2a874)"></span></td><td><b>Nam quis ligula a nibh fermentum venenatis vitae</b> nec neque. Etiam non felis mi. Quisque feugiat, lectus non feugiat consectetur,</td><td><b>Nam quis ligula a</b> nec neque. Etiam non felis mi.</td><td><b>Nam quis ligula</b> nec neque. Etiam non felis mi.</td><td class="price">$ 00.00</td></tr>
      <tr><td><span class="pic" role="img" aria-label="Wooden crate photo" style="background:linear-gradient(#8a7460,#4a3a2c)"></span></td><td><b>Nam quis ligula a nibh fermentum venenatis vitae</b> nec neque. Etiam non felis mi. Quisque feugiat, lectus non feugiat consectetur,</td><td><b>Nam quis ligula a</b> nec neque. Etiam non felis mi.</td><td><b>Nam quis ligula</b> nec neque. Etiam non felis mi.</td><td class="price">$ 00.00</td></tr>
      <tr><td><span class="pic" role="img" aria-label="Colourful gift boxes on blue photo" style="background:linear-gradient(#1e8fd6,#e5532f)"></span></td><td><b>Nam quis ligula a nibh fermentum venenatis vitae</b> nec neque. Etiam non felis mi. Quisque feugiat, lectus non feugiat consectetur,</td><td><b>Nam quis ligula a</b> nec neque. Etiam non felis mi.</td><td><b>Nam quis ligula</b> nec neque. Etiam non felis mi.</td><td class="price">$ 00.00</td></tr>
    </tbody>
  </table>
</main>

<footer>
  <div class="legal abs">Copyright © 2011-2013 CrateHarbor, Inc. All Rights Reserved. CrateHarbor.com is a trademark of CrateHarbor Inc.<br>Designated trademarks and brands are the property of their respective owners. Use of this Web site constitutes acceptance of the<br>CrateHarbor user agrement and privacy policy.</div>
  <div class="footer-links abs" style="left:109px">Privacy Policy<br>User Agreement<br>Help</div>
  <div class="footer-links abs" style="left:221px">About CrateHarbor.com<br>News and Articles<br>Contact Information</div>
  <div class="footer-links abs" style="left:388px">Glossary<br>Container Dimensions and Weights<br>Browse Locations</div>
  <div class="footer-brand abs">CrateHarbor.com</div>
  <div class="bottom-bar abs">© Copyright 2013. All Rights Reserved.</div>
</footer>

</body>
</html>
```